Design some Business Cards for Professional Cleaning company

Double sided card/ Standard card (I believe 3.5" x 2")
Unique
I have a logo already (Which is awesome)
Contact info: Marta Quill
martaquill@thebrightcornercleaning.example
(404) 555-0182
thebrightcornercleaning.example
Servicing Atlanta and Surrounding Areas
List of my services somehow without it looking cluttered
-Commercial/ New Construction clean up
-Residential/ rental property turn over
-move ins/move outs (Tenant)
-Pre/Post Event Clean Up
-Office Cleaning
-Restaurants and more!
I am open and versatile and very appreciative

```html
<!DOCTYPE html>
<html lang="en">
<head>
<meta charset="utf-8">
<title>The Bright Corner — Business Cards</title>
<link rel="stylesheet" href="https://fonts.googleapis.com/css2?family=Cinzel:wght@500;600&family=Pathway+Gothic+One&display=swap">
<style>
  :root {
    --backdrop: #2b2d30;
    --card-dark: #26292b;
    --card-blue: #1f74cc;
    --ink-light: #f2f4f5;
    --ink-soft: #c9d2d8;
    --brand-blue: #3fb6ee;
    --brand-deep: #0d4f84;
    --shadow: rgba(0, 0, 0, 0.45);
  }
  * { box-sizing: border-box; margin: 0; padding: 0; }
  html, body { width: 1200px; height: 848px; overflow: hidden; }
  body {
    background: var(--backdrop);
    position: relative;
    font-family: "Pathway Gothic One", "Arial Narrow", sans-serif;
  }
  .card-sheet {
    position: absolute;
    inset: 0;
    display: grid;
    grid-template-columns: 525px 525px;
    grid-template-rows: 300px 300px;
    gap: 60px 50px;
    padding: 94px 50px;
  }
  .card {
    position: relative;
    width: 525px;
    height: 300px;
    border-radius: 4px;
    box-shadow: 0 10px 24px var(--shadow);
    overflow: hidden;
    color: var(--ink-light);
  }
  .card--dark { background: var(--card-dark); }
  .card--blue { background: var(--card-blue); }
  .card--spectrum {
    background:
      radial-gradient(circle at 15% 80%, #7a3fc4 0%, transparent 45%),
      radial-gradient(circle at 35% 20%, #e2823c 0%, transparent 40%),
      radial-gradient(circle at 70% 60%, #8fd16a 0%, transparent 45%),
      radial-gradient(circle at 90% 15%, #c064d8 0%, transparent 40%),
      linear-gradient(120deg, #5a4fd0, #d9b35c 45%, #7bcf8c 70%, #9a5ed6);
  }

  /* contact block */
  .contact {
    position: absolute;
    top: 34px;
    right: 40px;
    text-align: center;
    width: 300px;
  }
  .contact__name {
    font-family: "Cinzel", "Times New Roman", serif;
    font-weight: 600;
    font-size: 25px;
    letter-spacing: 2.5px;
    line-height: 1;
  }
  .contact__phone {
    font-family: "Cinzel", "Times New Roman", serif;
    font-weight: 500;
    font-size: 18px;
    letter-spacing: 2px;
    margin-top: 4px;
  }
  .contact__email {
    font-family: "Cinzel", "Times New Roman", serif;
    font-weight: 500;
    font-size: 9.5px;
    letter-spacing: 0.6px;
    margin-top: 4px;
    white-space: nowrap;
  }

  /* services list */
  .services {
    position: absolute;
    left: 34px;
    top: 118px;
    list-style: none;
    font-size: 15px;
    line-height: 1.42;
    letter-spacing: 0.6px;
  }

  /* brand lockup */
  .brand {
    position: absolute;
    right: 92px;
    top: 118px;
    width: 140px;
    text-align: center;
  }
  .brand__dot {
    display: block;
    width: 46px;
    height: 46px;
    border-radius: 50%;
    background: var(--brand-blue);
    margin: 0 auto 6px;
  }
  .brand__name {
    color: var(--brand-blue);
    font-size: 26px;
    line-height: 1;
    letter-spacing: 0.5px;
  }
  .card--blue .brand__name,
  .card--spectrum .brand__name { color: var(--brand-deep); }
  .card--blue .brand__dot,
  .card--spectrum .brand__dot { background: var(--brand-deep); }
  .brand__url {
    font-family: "Cinzel", "Times New Roman", serif;
    font-size: 8px;
    letter-spacing: 0.4px;
    color: var(--ink-soft);
    margin-top: 16px;
    white-space: nowrap;
  }
  .card--blue .brand__url,
  .card--spectrum .brand__url { color: var(--ink-light); }

  /* back side */
  .brand--back {
    left: 50%;
    top: 50%;
    right: auto;
    width: 240px;
    transform: translate(-50%, -50%);
  }
  .brand--back .brand__dot { width: 78px; height: 78px; margin-bottom: 12px; }
  .brand--back .brand__name { font-size: 42px; }
</style>
</head>
<body>
  <main class="card-sheet">

    <section class="card card--dark card--back" aria-label="Card back">
      <div class="brand brand--back">
        <span class="brand__dot"></span>
        <p class="brand__name">The Bright Corner</p>
      </div>
    </section>

    <section class="card card--dark" aria-label="Card front, dark">
      <div class="contact">
        <p class="contact__name">Marta Quill</p>
        <p class="contact__phone">(404) 555-0182</p>
        <p class="contact__email">martaquill@thebrightcornercleaning.example</p>
      </div>
      <ul class="services">
        <li>-Commercial/ New Construction clean up</li>
        <li>-Residential/ rental property turn over</li>
        <li>-move ins/move outs (Tenant)</li>
        <li>-Pre/Post Event Clean Up</li>
        <li>-Office Cleaning</li>
        <li>-Restaurants and more!</li>
      </ul>
      <div class="brand">
        <span class="brand__dot"></span>
        <p class="brand__name">The Bright Corner</p>
        <p class="brand__url">thebrightcornercleaning.example</p>
      </div>
    </section>

    <section class="card card--blue" aria-label="Card front, blue">
      <div class="contact">
        <p class="contact__name">Marta Quill</p>
        <p class="contact__phone">(404) 555-0182</p>
        <p class="contact__email">martaquill@thebrightcornercleaning.example</p>
      </div>
      <ul class="services">
        <li>-Commercial/ New Construction clean up</li>
        <li>-Residential/ rental property turn over</li>
        <li>-move ins/move outs (Tenant)</li>
        <li>-Pre/Post Event Clean Up</li>
        <li>-Office Cleaning</li>
        <li>-Restaurants and more!</li>
      </ul>
      <div class="brand">
        <span class="brand__dot"></span>
        <p class="brand__name">The Bright Corner</p>
        <p class="brand__url">thebrightcornercleaning.example</p>
      </div>
    </section>

    <section class="card card--spectrum" aria-label="Card front, spectrum">
      <div class="contact">
        <p class="contact__name">Marta Quill</p>
        <p class="contact__phone">(404) 555-0182</p>
        <p class="contact__email">martaquill@thebrightcornercleaning.example</p>
      </div>
      <ul class="services">
        <li>-Commercial/ New Construction clean up</li>
        <li>-Residential/ rental property turn over</li>
        <li>-move ins/move outs (Tenant)</li>
        <li>-Pre/Post Event Clean Up</li>
        <li>-Office Cleaning</li>
        <li>-Restaurants and more!</li>
      </ul>
      <div class="brand">
        <span class="brand__dot"></span>
        <p class="brand__name">The Bright Corner</p>
        <p class="brand__url">thebrightcornercleaning.example</p>
      </div>
    </section>

  </main>
</body>
</html>
```